Brise haute coffee - Label design

Watchout: Keep in mind while you submit it needs to be a LABEL (that will be sticked on brown kraft 250 g side gusset coffee pouches). No custom pack for time being (need more scale to custom print pack).

Looking for a label design for my new Doux Vent collection of freshly roasted, single origin specialty coffee. Brand name is Brise Haute (it means red earth and alludes to the soil coffee grows on at high altitude in Africa. It also alludes to the red color of the coffee fruit). Brand selling line is "Pure Origin Coffee". Label to go as stickers on 250 g side gusset coffee pouches in Kraft brown paper (will print labels and stick on packs, packs are 80 mm wide and 260 mm long). This is a relatively complex project comprising the "brise haute" brand logo (funded separately, winner will have the job), the "Doux Vent" collection visual identity, iconic assets for brand and collection recognition across lineup, educational visual icons, text placeholders. It needs to combine hard point visual elements and soft points (text placeholder) which I can easily edit on need basis (text needs to be "outlines" for easy editing after submission). Winner of label submission gets to design brand logo. I will ultimately need 3 different labels for our Doux Vent collection, one for each continent our coffee comes from (Africa, Asia, Latin America). This pitch should focus on the Africa one only. Winner will then have opportunity to design the other ones in consistent way.

BRIEF:
We roast single origin, high quality specialty coffee from high altitude estates in Africa (volcanic slopes in Congo and Burundi, Highlands in Ethiopia and Kenya) Design need to induce the premiumness of the proposition (this is a collection called "Doux Vent"), as well the the unique geographical origins of our coffee (without being too specific as we want to use same label for all our African origins) -oversized shape of continent in background + some visuals conveying the African roots could work well. It needs to create a mental Journey "back to the origins" - of mankind, of unique terroirs creating the best coffee, of our unspoilt roots. So the Journey themes is critical (to be expressed by the telegram type of font, by the way Africa is brought to life,etc.). At the same time keep in mind label space is limited (label stickers go on 250 g coffee pouches made in kraft brown paper) and we want to have a pure design, which leaves room to the text placeholder (see below) and is easily recognizable and reapplicable across the SKUs (we will add Asia and Latin America packs once we lock Africa). As such we need to strike right balance between visual differentiation by origin (Africa, Asia, Latin America) and common iconic assets for brand recognition and lineup harmonization (same font, same way the continent is brought to life, same structure of the label, differentiation by color background,etc.).

We need placeholder for text that will specify exact name of estate, county of origin, coffee type, roasting level and tasting notes. Here I will allow myself some creative direction: it should be in the format of a vintage luggage tag (see attached examples) where we can edit content in Telegram font (our coffee sourcing changes often). We will need to assess if the tag remains standard across collection, or whether we are able to give it a visual twist for each origin (Africa, Asia, Latin America). That would be nicer (see Morvelin "Stamps" example), but priority of the text placeholder is clarity of information above anything else.

Last nice to have (if it time allows) we need educational visual icons (ideally as separate small round labels we can stick on the pack above the main label) for recommended brewing method (filter, espresso, italian moka, french press).

Reason: Still looking for the design in line with brief. Will send feedback to the top 3 routes today.

Target Market(s)

Switzerland

Industry/Entity Type

Coffee Shop

Logo Text

Brise haute -Pure Origin Coffee

Font styles to use
Other font styles liked:
• TELEGRAM type of font to induce geographical journey, single origin,.. For the "luggage tag" placeholder

Requirements
Must have
• - Brand name: Brise Haute. Brand selling line: Pure Origin Coffee. Brand Logo: winner of label submission gets to design brand logo
• - Collection name: DOUX VENT (written, I can see well as a vertical block). name of SKU: AFRICA (visualized a must, written tbc).
• - Text place holder (vintage luggage tag in telegram font) : we will show there name of estate, country of origin, tasting notes. I could see nicely a baggage tag format, where we fill in the details in telegram type of font.
• - 100% single origin Arabica (at the bottom)
• - 250 g (at the bottom)
• Technical Specs:
• A. Artwork must be supplied in either Adobe illustrator or Adobe Photoshop files or Coral Draw files
• B. Create all text in artwork in ‘ outlines ’
• C. The resolution of photographic image files must be no less than 350 dpi
• D. Never flatten the file as we require all layers
• E. All Photoshop image files should be linked and attached. Never flatten the layers and do not change the directory
• F. Create the images with CMYK colour mode ( RGB colour mode is not for printing)
• G. If you are going to use a spot colour please reference the Pantone ( PMS #)
• H. Designate all ‘Transparent’ areas in the artwork with a custom Pantone colour as well as designating the layer’s name as ‘ Transparent’. Please indicate specifically which pantone colour is designated for the ‘transparent’ area.
• I. Reduce any barcodes to 85% as a minimum scale
Nice to have
• - educational simple visual icons on recommended brewing method (filer, italian moka, french press or espresso) as additional small stickers to stick above main label

```html
<!DOCTYPE html>
<html lang="en">
<head>
<meta charset="utf-8">
<title>Brise Haute – Doux Vent coffee labels</title>
<link rel="stylesheet" href="https://fonts.googleapis.com/css2?family=Cutive+Mono&family=Oswald:wght@600&family=Special+Elite&display=swap">
<style>
  :root{
    --page:#ffffff;
    --card-line:#1a1a1a;
    --dots:#8a8a8a;
    --brand:#9b2b23;
    --paper:#e9e3cd;
    --paper-light:#f6f2e2;
    --field-ink:#4a463e;
    --rule:#d9cfa6;
    --blue-ink:#2486c0;
    --red-ink:#e0242a;
    --bottom-ink:#222222;
  }
  html,body{margin:0;padding:0;}
  body{width:686px;height:1200px;overflow:hidden;background:var(--page);position:relative;}
  .defs{position:absolute;width:0;height:0;}
  .label{position:absolute;width:268px;height:555px;}
  .label svg{display:block;width:100%;height:100%;}
  .label--honduras-a{left:40px;top:42px;}
  .label--honduras-b{left:349px;top:42px;}
  .label--ethiopia-a{left:40px;top:629px;}
  .label--ethiopia-b{left:349px;top:629px;}
  .card-frame{fill:var(--page);stroke:var(--card-line);stroke-width:1.4;}
  .card-dots{fill:none;stroke:var(--dots);stroke-width:1;stroke-dasharray:1.5 2;}
  .brand-ring{fill:none;stroke:var(--brand);stroke-width:1.5;}
  .brand-name{font-family:"Cutive Mono",monospace;font-size:17px;fill:var(--brand);letter-spacing:3px;}
  .collection{font-family:"Cutive Mono",monospace;font-size:29px;fill:#ffffff;letter-spacing:1px;}
  .field{font-family:"Special Elite",monospace;font-size:12px;fill:var(--field-ink);letter-spacing:.5px;}
  .field-rule{stroke:var(--rule);stroke-width:1;}
  .origin-word{font-family:"Oswald",sans-serif;font-weight:600;font-size:41px;letter-spacing:-.5px;}
  .origin--blue .origin-word{fill:var(--blue-ink);}
  .origin--blue .origin-box{stroke:var(--blue-ink);}
  .origin--red .origin-word{fill:var(--red-ink);}
  .origin--red .origin-box{stroke:var(--red-ink);}
  .origin-box{fill:none;}
  .claim{font-family:"Cutive Mono",monospace;font-size:15px;fill:var(--bottom-ink);font-variant:small-caps;letter-spacing:1px;}
  .weight{font-family:"Cutive Mono",monospace;font-size:15px;fill:var(--bottom-ink);letter-spacing:2px;}
</style>
</head>
<body>

<svg class="defs" aria-hidden="true">
  <defs>
    <linearGradient id="tag-blue" x1="0" y1="0" x2="1" y2="1">
      <stop offset="0" stop-color="#1d6e9c"/>
      <stop offset=".45" stop-color="#3a93bf"/>
      <stop offset="1" stop-color="#175a86"/>
    </linearGradient>
    <linearGradient id="tag-red" x1="0" y1="0" x2="1" y2="1">
      <stop offset="0" stop-color="#a8141b"/>
      <stop offset=".45" stop-color="#d8252b"/>
      <stop offset="1" stop-color="#8c0f14"/>
    </linearGradient>
    <radialGradient id="paper-glow" cx=".5" cy=".45" r=".7">
      <stop offset="0" stop-color="var(--paper-light)" style="stop-color:#f7f3e3"/>
      <stop offset="1" stop-color="#dcd5bc"/>
    </radialGradient>
    <linearGradient id="flag-honduras" x1="0" y1="0" x2="0" y2="1">
      <stop offset="0" stop-color="#2f7fc1"/>
      <stop offset=".33" stop-color="#2f7fc1"/>
      <stop offset=".34" stop-color="#f1f1f1"/>
      <stop offset=".66" stop-color="#f1f1f1"/>
      <stop offset=".67" stop-color="#2f7fc1"/>
      <stop offset="1" stop-color="#2f7fc1"/>
    </linearGradient>
    <linearGradient id="flag-ethiopia" x1="0" y1="0" x2="0" y2="1">
      <stop offset="0" stop-color="#3f9a3a"/>
      <stop offset=".5" stop-color="#e8c733"/>
      <stop offset="1" stop-color="#d8312a"/>
    </linearGradient>
    <pattern id="chevrons" width="14" height="10" patternUnits="userSpaceOnUse">
      <path d="M3 2 L9 5 L3 8 Z" fill="#ffffff"/>
    </pattern>
    <filter id="tag-shadow" x="-10%" y="-10%" width="130%" height="130%">
      <feGaussianBlur stdDeviation="3"/>
    </filter>

    <symbol id="card-base" viewBox="0 0 332 688">
      <rect class="card-frame" x="0.7" y="0.7" width="330.6" height="686.6"/>
      <rect class="card-dots" x="9.5" y="10.5" width="313" height="667"/>
      <circle class="brand-ring" cx="166" cy="84" r="54"/>
      <text class="brand-name" x="166" y="80" text-anchor="middle">BRISE</text>
      <text class="brand-name" x="166" y="101" text-anchor="middle">HAUTE</text>
      <text class="claim" x="166" y="632" text-anchor="middle">100% single origin Arabica</text>
      <text class="weight" x="166" y="662" text-anchor="middle">250 g</text>
    </symbol>

    <symbol id="tag-fields" viewBox="0 0 332 688">
      <rect x="58" y="286" width="214" height="300" fill="url(#paper-glow)"/>
      <path d="M62 362 l6 -2 l0 -4 l2 0 l1 4 l8 -1 l0 3 l-8 1 l-1 4 l-2 0 l0 -4 l-6 -2 z" fill="#1e1e1e"/>
      <text class="field" x="63" y="390">Estate</text>
      <line class="field-rule" x1="60" y1="416" x2="270" y2="416"/>
      <line class="field-rule" x1="60" y1="428" x2="270" y2="428"/>
      <text class="field" x="63" y="445">Character</text>
      <line class="field-rule" x1="60" y1="472" x2="270" y2="472"/>
      <line class="field-rule" x1="60" y1="484" x2="270" y2="484"/>
      <text class="field" x="63" y="502">Roasting date</text>
      <rect x="50" y="243" width="230" height="10" fill="url(#chevrons)"/>
      <rect x="50" y="590" width="230" height="10" fill="url(#chevrons)"/>
    </symbol>

    <symbol id="tag-eyelet" viewBox="0 0 332 688">
      <circle cx="163" cy="207" r="27" fill="#d8be8e"/>
      <circle cx="163" cy="207" r="15" fill="#ffffff"/>
    </symbol>
  </defs>
</svg>

<!-- Latin America: Honduras, with collection name -->
<div class="label label--honduras-a">
  <svg viewBox="0 0 332 688" role="img" aria-label="Brise Haute Doux Vent label, Honduras">
    <use href="#card-base"/>
    <path d="M101 164 H241 L286 214 V609 H56 V214 Z" fill="#000" opacity=".35" filter="url(#tag-shadow)"/>
    <path class="tag" d="M95 158 H235 L280 208 V603 H50 V208 Z" fill="url(#tag-blue)"/>
    <use href="#tag-eyelet"/>
    <text class="collection" x="166" y="280" text-anchor="middle">DOUX VENT</text>
    <use href="#tag-fields"/>
    <g class="origin origin--blue" transform="rotate(-4 175 330)">
      <rect class="origin-box" x="85" y="298" width="182" height="62" stroke-width="3.5"/>
      <rect class="origin-box" x="91" y="304" width="170" height="50" stroke-width="1.5"/>
      <text class="origin-word" x="176" y="346" text-anchor="middle">HONDURAS</text>
    </g>
    <rect x="58" y="514" width="98" height="76" fill="#f4f1e8"/>
    <rect x="63" y="519" width="88" height="66" fill="#3f6d9e" role="img" aria-label="Vintage Honduras airmail postage stamp"/>
    <rect x="162" y="514" width="110" height="66" fill="url(#flag-honduras)" role="img" aria-label="Honduras flag with postmark"/>
  </svg>
</div>

<div class="label label--honduras-b">
  <svg viewBox="0 0 332 688" role="img" aria-label="Brise Haute label, Honduras">
    <use href="#card-base"/>
    <path d="M101 164 H241 L286 214 V609 H56 V214 Z" fill="#000" opacity=".35" filter="url(#tag-shadow)"/>
    <path class="tag" d="M95 158 H235 L280 208 V603 H50 V208 Z" fill="url(#tag-blue)"/>
    <use href="#tag-eyelet"/>
    <use href="#tag-fields"/>
    <g class="origin origin--blue" transform="rotate(-4 175 330)">
      <rect class="origin-box" x="85" y="298" width="182" height="62" stroke-width="3.5"/>
      <rect class="origin-box" x="91" y="304" width="170" height="50" stroke-width="1.5"/>
      <text class="origin-word" x="176" y="346" text-anchor="middle">HONDURAS</text>
    </g>
    <rect x="58" y="514" width="98" height="76" fill="#f4f1e8"/>
    <rect x="63" y="519" width="88" height="66" fill="#3f6d9e" role="img" aria-label="Vintage Honduras airmail postage stamp"/>
    <rect x="162" y="514" width="110" height="66" fill="url(#flag-honduras)" role="img" aria-label="Honduras flag with postmark"/>
  </svg>
</div>

<!-- Africa: Ethiopia -->
<div class="label label--ethiopia-a">
  <svg viewBox="0 0 332 688" role="img" aria-label="Brise Haute Doux Vent label, Ethiopia">
    <use href="#card-base"/>
    <path d="M101 164 H241 L286 214 V609 H56 V214 Z" fill="#000" opacity=".35" filter="url(#tag-shadow)"/>
    <path class="tag" d="M95 158 H235 L280 208 V603 H50 V208 Z" fill="url(#tag-red)"/>
    <use href="#tag-eyelet"/>
    <text class="collection" x="166" y="280" text-anchor="middle">DOUX VENT</text>
    <use href="#tag-fields"/>
    <g class="origin origin--red" transform="rotate(-4 175 330)">
      <rect class="origin-box" x="85" y="298" width="182" height="62" stroke-width="3.5"/>
      <rect class="origin-box" x="91" y="304" width="170" height="50" stroke-width="1.5"/>
      <text class="origin-word" x="176" y="346" text-anchor="middle">ETHIOPIA</text>
    </g>
    <rect x="58" y="514" width="110" height="74" fill="#f4f1e8"/>
    <rect x="63" y="519" width="100" height="64" fill="#c23a33" role="img" aria-label="Vintage Ethiopian postage stamp"/>
    <rect x="172" y="512" width="100" height="70" fill="url(#flag-ethiopia)" role="img" aria-label="Ethiopian flag with postmark"/>
  </svg>
</div>

<div class="label label--ethiopia-b">
  <svg viewBox="0 0 332 688" role="img" aria-label="Brise Haute label, Ethiopia">
    <use href="#card-base"/>
    <path d="M101 164 H241 L286 214 V609 H56 V214 Z" fill="#000" opacity=".35" filter="url(#tag-shadow)"/>
    <path class="tag" d="M95 158 H235 L280 208 V603 H50 V208 Z" fill="url(#tag-red)"/>
    <use href="#tag-eyelet"/>
    <use href="#tag-fields"/>
    <g class="origin origin--red" transform="rotate(-4 175 330)">
      <rect class="origin-box" x="85" y="298" width="182" height="62" stroke-width="3.5"/>
      <rect class="origin-box" x="91" y="304" width="170" height="50" stroke-width="1.5"/>
      <text class="origin-word" x="176" y="346" text-anchor="middle">ETHIOPIA</text>
    </g>
    <rect x="58" y="514" width="110" height="74" fill="#f4f1e8"/>
    <rect x="63" y="519" width="100" height="64" fill="#c23a33" role="img" aria-label="Vintage Ethiopian postage stamp"/>
    <rect x="172" y="512" width="100" height="70" fill="url(#flag-ethiopia)" role="img" aria-label="Ethiopian flag with postmark"/>
  </svg>
</div>

</body>
</html>
```